Hire OKRIM

We are developing a website that allows Hospitality employees to apply for hospitality jobs in the OKRIM union. They do this by completing a standarized application form.

The wirefram lays out all of the pages and how they are conected.

The focus is on functinality, simplicity and intuitive.

The site will be in Thai and English.

We're looking for a mok up the first page only to evaluate designs. If we're able to find a design that works, we would ask for the all pages of the wireframe to be completed as per the alocated budget.

Thanks to all the designers for the initial landing pagedesign.  We have committed topayment for a finished design of all 11 pages and windows as per our attachedwireframe.  We would like to choosea final designer by Monday the 7th.x

Reason: We have committed to payment for a finished design of all 11 pages and windows as per our attached wireframe. We would like to choose a final designer by Monday the 7th.

Target Market(s)

Thai nationals ages 20-30 that work in the hospitality industry.

Industry/Entity Type

Hospitality

Colors

Designer to choose colors to be used in the design.

Requirements
Must have
• Intuitive layout
Simple and clean - no redundancy.

```html
<!DOCTYPE html>
<html lang="en">
<head>
<meta charset="utf-8">
<title>Hire OKRIM</title>
<link rel="stylesheet" href="https://fonts.googleapis.com/css2?family=Open+Sans:ital,wght@0,400;0,600;0,700;1,600&display=swap">
<style>
:root{
  --bar:#1f1f1f;
  --footer:#232323;
  --white:#ffffff;
  --ink:#333333;
  --green:#a5cf33;
  --panel:rgba(22,22,22,.86);
  --muted:#e6e6e6;
}
*{box-sizing:border-box;margin:0;padding:0}
html,body{width:1200px;height:860px;overflow:hidden}
body{position:relative;font-family:"Open Sans",Arial,sans-serif;background:var(--white);color:var(--ink)}
.topbar{position:absolute;left:0;top:0;width:1200px;height:40px;background:var(--bar);color:var(--muted);font-size:13px}
.lang{position:absolute;left:108px;top:13px}
.lang span{font-size:10px;margin-left:6px}
.welcome{position:absolute;right:208px;top:12px}
.welcome a{color:var(--muted);margin-left:6px}
.social{position:absolute;left:1034px;top:7px;display:flex;gap:6px}
.social span{width:28px;height:28px;border:2px solid var(--muted);border-radius:50%;display:block}
.header{position:absolute;left:0;top:40px;width:1200px;height:90px;background:var(--white)}
.brand-name{position:absolute;left:104px;top:24px;font-size:30px;font-weight:700;color:var(--ink);line-height:40px}
.nav-contact{position:absolute;left:895px;top:34px;font-size:19px;font-weight:700;color:var(--ink)}
.nav-login{position:absolute;left:992px;top:21px;width:102px;height:46px;background:var(--green);color:var(--white);font-size:18px;font-weight:700;line-height:46px;padding-left:15px}
.nav-login span{font-size:13px;margin-left:8px}
.hero{position:absolute;left:0;top:130px;width:1200px;height:675px;background:radial-gradient(ellipse at 50% 35%,#a99482 0%,#5e4c3f 40%,#2a211c 75%,#1a1512 100%)}
.headline{position:absolute;left:-42px;top:428px;width:1200px;text-align:center;font-size:46px;font-weight:600;font-style:italic;color:var(--white);text-shadow:3px 3px 3px rgba(0,0,0,.8)}
.signup{position:absolute;top:530px;width:493px;height:192px;background:var(--panel);padding:0 12px 0 21px}
.signup.job{left:99px}
.signup.staff{left:609px}
.signup h2{text-align:center;font-size:30px;font-weight:700;color:var(--white);margin-top:15px;height:53px}
.fields{display:flex;gap:8px}
.field{flex:1;height:45px;background:var(--white);color:#444;font-size:16px;line-height:48px;padding-left:15px}
.btn{margin-top:8px;height:47px;background:var(--green);color:var(--white);font-size:18px;font-weight:600;text-align:center;line-height:47px}
.footer{position:absolute;left:0;top:805px;width:1200px;height:55px;background:var(--footer);color:var(--muted);font-size:12.8px}
.footer-links{position:absolute;left:104px;top:21px}
.copyright{position:absolute;right:100px;top:21px}
</style>
</head>
<body>
<div class="topbar">
  <div class="lang">English<span>▼</span></div>
  <div class="welcome">Welcome to hireokrim.com, jobseekers please<a href="#">register</a></div>
  <div class="social"><span></span><span></span></div>
</div>
<header class="header">
  <div class="brand-name">Hire OKRIM</div>
  <div class="nav-contact">Contact</div>
  <div class="nav-login">Login<span>▼</span></div>
</header>
<section class="hero" role="img" aria-label="Photo of a smiling waitress serving an older couple at a restaurant table with wine glasses"></section>
<h1 class="headline">Hire the Competent PROFESSIONALS</h1>
<form class="signup job">
  <h2>I WANT JOB?</h2>
  <div class="fields"><div class="field">Name...</div><div class="field">Email..</div></div>
  <div class="btn">Sign Up Now</div>
</form>
<form class="signup staff">
  <h2>WE WANT STAFF?</h2>
  <div class="fields"><div class="field">Company Name...</div><div class="field">Email..</div></div>
  <div class="btn">Sign Up Now</div>
</form>
<footer class="footer">
  <div class="footer-links">About Us | FAQ's | Terms of Use | Privacy | Contact Us | Site Map</div>
  <div class="copyright">Copyright © 2014 hireokrim.com. All rights reserved.</div>
</footer>
</body>
</html>
```